Tindral

CD cover for an eclectic DJ mix that features deep ambient electronica taking the listener on a journey of the mind and the cosmos, highlighting we are all connected.
Cerebral, emotional, evocative music that's non commercial.
Can provide a soundbyte or two if required.

Target Market(s)

Discernable listeners that like to discover new sounds.

Requirements
Nice to have
• Layered, subtle

```html
<!DOCTYPE html>
<html lang="en">
<head>
<meta charset="utf-8">
<title>Tindral — Album Cover</title>
<link rel="stylesheet" href="https://fonts.googleapis.com/css2?family=Michroma&display=swap">
<style>
  :root {
    --space-deep: #07050f;
    --space-indigo: #1a1238;
    --nebula-violet: #6b55a8;
    --nebula-gold: #c79a55;
    --haze-lilac: #8c7fc4;
    --title-ink: #e9e8ef;
  }
  html, body {
    margin: 0;
    padding: 0;
    width: 1194px;
    height: 1200px;
    overflow: hidden;
    background: var(--space-deep);
  }
  .cover {
    position: relative;
    width: 1194px;
    height: 1200px;
    overflow: hidden;
    background:
      radial-gradient(ellipse 60% 30% at 55% 100%, rgba(140,127,196,0.55), transparent 70%),
      radial-gradient(ellipse 50% 35% at 85% 30%, rgba(199,154,85,0.35), transparent 70%),
      radial-gradient(ellipse 70% 40% at 40% 15%, rgba(107,85,168,0.45), transparent 70%),
      linear-gradient(180deg, var(--space-indigo) 0%, var(--space-deep) 70%, #1b1533 100%);
  }
  .artwork {
    position: absolute;
    border-radius: 50%;
  }
  .artwork--veil {
    left: 0; top: 0;
    width: 880px; height: 760px;
    border-radius: 0 40% 45% 0 / 0 30% 55% 0;
    background:
      radial-gradient(ellipse 40% 35% at 20% 15%, rgba(199,154,85,0.85), transparent 70%),
      radial-gradient(ellipse 45% 40% at 55% 70%, rgba(199,154,85,0.6), transparent 70%),
      linear-gradient(160deg, #b99a6a 0%, #5d4a93 35%, #3a2a66 60%, #8a6d4c 100%);
    opacity: 0.85;
  }
  .artwork--planet-blue {
    left: 890px; top: 258px;
    width: 168px; height: 168px;
    background: radial-gradient(circle at 40% 35%, #9aa0b8, #3a3e55 70%, #151624);
  }
  .artwork--planet-gold {
    left: 795px; top: 485px;
    width: 208px; height: 208px;
    background: radial-gradient(circle at 45% 40%, #d9b680, #8a6a3c 60%, #2a1f14);
  }
  .artwork--planet-moon {
    left: -40px; top: 775px;
    width: 210px; height: 380px;
    border-radius: 0 50% 50% 0 / 0 50% 50% 0;
    background: radial-gradient(circle at 30% 30%, #d8c79a, #6b5a8a 60%, #1f1838);
  }
  .strands {
    position: absolute;
    inset: 0;
  }
  .title-line {
    position: absolute;
    left: 185px;
    top: 808px;
    display: flex;
    align-items: baseline;
    gap: 26px;
    color: var(--title-ink);
    font-family: "Michroma", sans-serif;
    white-space: nowrap;
  }
  .title-line__artist {
    font-size: 31px;
    letter-spacing: 0.42em;
  }
  .title-line__album {
    font-size: 54px;
    letter-spacing: 0.38em;
  }
</style>
</head>
<body>
  <main class="cover">
    <div class="artwork artwork--veil" role="img" aria-label="Translucent flowing veil of cosmic mist in violet and gold"></div>
    <div class="artwork artwork--planet-blue" role="img" aria-label="Small planet with cloud-covered surface"></div>
    <div class="artwork artwork--planet-gold" role="img" aria-label="Glass sphere holding a golden moon"></div>
    <div class="artwork artwork--planet-moon" role="img" aria-label="Cratered moon rising at the left edge"></div>

    <svg class="strands" width="1194" height="1200" viewBox="0 0 1194 1200" aria-hidden="true">
      <g fill="none" stroke="#e8d3a6" stroke-linecap="round">
        <path d="M875 60 L712 780" stroke-width="3" opacity="0.85"/>
        <path d="M862 140 L860 455" stroke-width="2" opacity="0.7"/>
        <path d="M875 60 L1180 850" stroke-width="1.6" opacity="0.5"/>
        <path d="M880 75 L1194 480" stroke-width="1" opacity="0.35"/>
      </g>
    </svg>

    <h1 class="title-line">
      <span class="title-line__artist">ARTIST NAME</span>
      <span class="title-line__album">TINDRAL</span>
    </h1>
  </main>
</body>
</html>
```